Orthopedic Arm Surgeon Brochure

Bifold modern design. I will supply the text, my photo, and photos of my textbooks. Prefer colors in the greens, blues, greys. For more information visit MendLimbWellDallas.example Please feel free to e-mail me with any questions. Current brochure attached; I want to modernize this, get rid of frames, and change the text.

Target Market(s)

High-end market

Colors
3176b5
33a6d7
33b8a4
abd036
876aae
b768aa

Requirements
Must have
• Beautiful finishes
Should not have
• Bright reds, yellows, oranges that emit fear

```html
<!DOCTYPE html>
<html lang="en">
<head>
<meta charset="utf-8">
<title>Orthopedic Arm Surgeon Brochure</title>
<link rel="stylesheet" href="https://fonts.googleapis.com/css2?family=Roboto+Condensed:ital,wght@0,300;0,400;0,700;1,700&family=Open+Sans:wght@400;600;700&display=swap">
<style>
:root{
  --navy:#0b2f86;
  --royal:#1d5cc0;
  --blue:#3176b5;
  --sky:#33a6d7;
  --teal:#33b8a4;
  --green:#1f9a7a;
  --ink:#3a4150;
  --paper:#ffffff;
  --stage:#e8e9ec;
  --pale:#eef4fa;
}
*{box-sizing:border-box;margin:0;padding:0}
html,body{width:1200px;height:2511px;overflow:hidden;background:var(--stage)}
body{position:relative;font-family:"Open Sans",sans-serif;color:var(--ink)}
.page{position:absolute;width:560px;height:792px;background:var(--paper);overflow:hidden}
.front-solo{top:22px;left:320px;box-shadow:0 6px 18px rgba(0,0,0,.12)}
.spread{position:absolute;left:40px;width:1120px;height:792px;box-shadow:0 6px 18px rgba(0,0,0,.12)}
.spread-outside{top:854px}
.spread-inside{top:1686px}
.spread .page.left{left:0}
.spread .page.right{left:560px}
.abs{position:absolute}

/* front cover */
.hero{position:absolute;left:0;top:0;width:560px;height:420px}
.inset{position:absolute;left:22px;top:232px;width:150px;height:150px;border-radius:50%;border:6px solid var(--teal);background:radial-gradient(circle at 45% 45%,#5b8fe0,#18479e 75%)}
.brand{position:absolute;display:flex;align-items:center;gap:6px;font-family:"Roboto Condensed",sans-serif;font-weight:700;color:var(--green);line-height:1}
.brand .dot{width:14px;height:14px;border-radius:50%;background:var(--green);flex:none}
.brand .name{font-size:19px}
.brand small{display:block;font-size:11px;font-weight:700;margin-top:2px}
.front .brand{left:345px;top:378px}
.title-block{position:absolute;left:34px;top:432px;width:500px;font-family:"Roboto Condensed",sans-serif;font-style:italic;font-weight:700;line-height:1.02}
.doctor{color:var(--blue);font-size:17px}
.specialty{color:var(--royal);font-size:38px}
.regions{color:var(--green);font-size:19px}
.board{color:var(--teal);font-size:31px}
.cert{color:var(--sky);font-style:normal;font-weight:300;font-size:14.5px;margin-top:3px;letter-spacing:.3px}
.conditions{position:absolute;left:34px;top:618px;width:500px;display:grid;grid-template-columns:1.05fr 1fr .9fr;gap:4px 14px;font-size:12.5px;color:var(--ink)}
.conditions li{list-style:none;display:flex;align-items:center;gap:5px}
.tick{width:10px;height:10px;flex:none}
.rule{position:absolute;left:34px;top:676px;width:500px;height:2px;background:var(--sky)}
.callbar{position:absolute;left:0;bottom:0;width:560px;height:62px;background:linear-gradient(90deg,var(--royal),var(--blue));display:flex;align-items:center;padding:0 22px;color:#fff}
.callbar .phone{font-family:"Roboto Condensed",sans-serif;font-weight:700;font-size:24px;padding-right:12px;border-right:2px solid rgba(255,255,255,.6)}
.callbar .booking{padding-left:12px;font-size:12px;line-height:1.25}
.callbar .booking strong{font-size:14px;font-weight:600;display:block}

/* back cover */
.back .brand{left:26px;top:42px}
.bio{position:absolute;left:26px;top:82px;width:510px;font-size:9.5px;line-height:1.5}
.bio p+p{margin-top:5px}
.dr-tab{position:absolute;left:20px;top:214px;padding:5px 14px;background:var(--teal);color:#fff;font-family:"Roboto Condensed",sans-serif;font-weight:700;font-size:16px;border-radius:0 14px 14px 0}
.portrait{position:absolute;left:22px;top:248px;width:170px;height:170px;border-radius:50%;border:6px solid var(--teal);background:linear-gradient(160deg,#c9d3de,#5c6b7c);z-index:2}
.books{position:absolute;left:220px;top:240px;width:200px;height:120px;background:linear-gradient(120deg,#7b3e4a,#3c5a7a 55%,#a8793f)}
.back-band{position:absolute;left:0;top:0;width:560px;height:792px}
.locations{position:absolute;left:30px;top:450px;width:440px;color:#fff}
.locations h2{font-family:"Roboto Condensed",sans-serif;font-weight:700;font-size:19px;line-height:1.15;margin-bottom:12px}
.locations li{list-style:none;display:flex;gap:8px;font-size:13px;line-height:1.3;margin-bottom:9px}
.pin{width:11px;height:14px;flex:none;margin-top:2px}

/* inside */
.section-title{font-family:"Roboto Condensed",sans-serif;font-weight:700;font-size:18px;color:var(--teal)}
.body-copy{font-size:9.5px;line-height:1.55}
.body-copy p+p{margin-top:6px}
.carpal{position:absolute;left:170px;top:48px;width:360px}
.carpal-more{position:absolute;left:30px;top:218px;width:500px}
.arm-photo{position:absolute;left:0;top:392px;width:560px;height:190px;background:linear-gradient(100deg,#eef0f3,#d8dde4 60%,#f4f5f7)}
.pill{position:absolute;left:320px;top:562px;padding:7px 18px;border-radius:18px;background:var(--teal);color:#fff;font-family:"Roboto Condensed",sans-serif;font-weight:700;font-size:16px}
.cubital-copy{position:absolute;left:30px;top:640px;width:500px;color:#fff}
.trigger-panel{position:absolute;left:0;top:58px;width:560px;height:290px}
.trigger{position:absolute;left:40px;top:110px;width:490px;color:#fff}
.trigger .section-title{color:#fff}
.thumbs{position:absolute;left:40px;top:372px;width:490px;display:flex;gap:12px}
.thumbs div{flex:1;height:92px}
.thumb-a{background:linear-gradient(130deg,#e9dcd3,#b9c6d6)}
.thumb-b{background:linear-gradient(130deg,#f2e4da,#cdb8a8)}
.thumb-c{background:linear-gradient(130deg,#e3d6cf,#8b97a8)}
.wrist{position:absolute;left:40px;top:490px;width:490px}
.wrist .section-title{color:var(--sky)}
.wrist-bar{position:absolute;right:-20px;bottom:26px;width:240px;height:22px;border-radius:11px;background:var(--royal)}
</style>
</head>
<body>

<!-- Front cover -->
<section class="page front front-solo">
  <svg class="hero" viewBox="0 0 560 420" role="img" aria-label="Illustration of a glowing anatomical figure with highlighted elbow and wrist joints">
    <defs>
      <radialGradient id="heroGlowA" cx="60%" cy="35%" r="70%">
        <stop offset="0" stop-color="#6aa2ff"/><stop offset=".5" stop-color="#1d5cc0"/><stop offset="1" stop-color="#0b2f86"/>
      </radialGradient>
    </defs>
    <path d="M0 0H560V250C450 300 300 330 0 350Z" fill="url(#heroGlowA)"/>
    <path d="M0 350C300 330 450 300 560 250V272C450 322 300 352 0 372Z" fill="#33a6d7"/>
    <path d="M0 372C300 352 450 322 560 272V286C450 336 300 366 0 386Z" fill="#33b8a4" opacity=".7"/>
  </svg>
  <div class="inset" role="img" aria-label="Close-up illustration of an inflamed elbow joint"></div>
  <div class="brand"><span class="dot"></span><span><span class="name">LONESTAR</span><small>Limb Clinic, L.L.P</small></span></div>
  <div class="title-block">
    <div class="doctor">DANIEL R. HASKELL, MD</div>
    <div class="specialty">SPECIALIST IN SURGERY</div>
    <div class="regions">OF THE HAND, WRIST, ELBOW &amp; SHOULDER</div>
    <div class="board">BOARD CERTIFIED ORTHOPEDIC SURGEON</div>
    <div class="cert">CERTIFICATE OF ADDITIONAL QUALIFICATION, HAND SURGERY</div>
  </div>
  <ul class="conditions">
    <li><svg class="tick" viewBox="0 0 10 10"><path d="M1 5l3 3 5-7" fill="none" stroke="#3a4150" stroke-width="1.6"/></svg>Carpal Tunnel</li>
    <li><svg class="tick" viewBox="0 0 10 10"><path d="M1 5l3 3 5-7" fill="none" stroke="#3a4150" stroke-width="1.6"/></svg>Cubital Tunnel</li>
    <li><svg class="tick" viewBox="0 0 10 10"><path d="M1 5l3 3 5-7" fill="none" stroke="#3a4150" stroke-width="1.6"/></svg>Trigger Finger</li>
    <li><svg class="tick" viewBox="0 0 10 10"><path d="M1 5l3 3 5-7" fill="none" stroke="#3a4150" stroke-width="1.6"/></svg>Dequervain's Tendinitis</li>
    <li><svg class="tick" viewBox="0 0 10 10"><path d="M1 5l3 3 5-7" fill="none" stroke="#3a4150" stroke-width="1.6"/></svg>Elbow &amp; Shoulder Pain</li>
  </ul>
  <div class="rule"></div>
  <div class="callbar">
    <span class="phone">555-014-ARMS</span>
    <span class="booking"><strong>Appointments can be made online</strong>through bookvisit.example www.MendLimbWellDallas.example</span>
  </div>
</section>

<!-- Outside spread -->
<div class="spread spread-outside">
  <section class="page back left">
    <svg class="back-band" viewBox="0 0 560 792" aria-hidden="true">
      <defs>
        <linearGradient id="backBlue" x1="0" y1="0" x2="0" y2="1">
          <stop offset="0" stop-color="#33a6d7"/><stop offset="1" stop-color="#3176b5"/>
        </linearGradient>
      </defs>
      <path d="M0 300H560V792H0Z" fill="url(#backBlue)"/>
      <path d="M560 300C470 300 410 360 410 430C410 500 470 560 560 560Z" fill="#eef4fa"/>
      <path d="M0 300H400C410 340 420 360 440 372C300 380 150 400 0 430Z" fill="#ffffff"/>
      <path d="M0 430C150 400 300 380 440 372" fill="none" stroke="#33b8a4" stroke-width="5"/>
    </svg>
    <div class="brand"><span class="dot"></span><span><span class="name">LONESTAR</span><small>Limb Clinic, L.L.P</small></span></div>
    <div class="bio">
      <p>Dr. Haskell is a nationally recognized hand and upper limb surgeon who has edited several textbooks, published many original research papers and written numerous book chapters.</p>
      <p>Dr. Haskell graduated with honors from a leading university and completed his orthopedic residency and fellowship training in hand and upper extremity surgery. He is board certified in orthopedic surgery and holds a certificate of additional qualification in hand surgery.</p>
    </div>
    <div class="dr-tab">DR. HASKELL</div>
    <div class="portrait" role="img" aria-label="Portrait photo of the surgeon in a dark suit"></div>
    <div class="books" role="img" aria-label="Photo of the surgeon's published textbooks"></div>
    <div class="locations">
      <h2>DR. HASKELL SEES PATIENTS AT THE FOLLOWING LOCATIONS:</h2>
      <ul>
        <li><svg class="pin" viewBox="0 0 11 14"><path d="M5.5 0A5.5 5.5 0 0 0 0 5.5C0 9 5.5 14 5.5 14S11 9 11 5.5A5.5 5.5 0 0 0 5.5 0Zm0 7.5a2 2 0 1 1 0-4 2 2 0 0 1 0 4Z" fill="#fff"/></svg><span>Riverbend medical center<br>4120 Elm street suite 300 Dallas, Texas 75201</span></li>
        <li><svg class="pin" viewBox="0 0 11 14"><path d="M5.5 0A5.5 5.5 0 0 0 0 5.5C0 9 5.5 14 5.5 14S11 9 11 5.5A5.5 5.5 0 0 0 5.5 0Zm0 7.5a2 2 0 1 1 0-4 2 2 0 0 1 0 4Z" fill="#fff"/></svg><span>Cedar Park<br>2280 Oakline drive suite 110 Dallas, Texas 75204</span></li>
        <li><svg class="pin" viewBox="0 0 11 14"><path d="M5.5 0A5.5 5.5 0 0 0 0 5.5C0 9 5.5 14 5.5 14S11 9 11 5.5A5.5 5.5 0 0 0 5.5 0Zm0 7.5a2 2 0 1 1 0-4 2 2 0 0 1 0 4Z" fill="#fff"/></svg><span>Westfield<br>815 Maple Grove dr. Dallas, Texas 75206</span></li>
        <li><svg class="pin" viewBox="0 0 11 14"><path d="M5.5 0A5.5 5.5 0 0 0 0 5.5C0 9 5.5 14 5.5 14S11 9 11 5.5A5.5 5.5 0 0 0 5.5 0Zm0 7.5a2 2 0 1 1 0-4 2 2 0 0 1 0 4Z" fill="#fff"/></svg><span>Northgate<br>9300 Ridge road west Dallas, Texas 75230</span></li>
      </ul>
    </div>
  </section>

  <section class="page front right">
    <svg class="hero" viewBox="0 0 560 420" role="img" aria-label="Illustration of a glowing anatomical figure with highlighted elbow and wrist joints">
      <defs>
        <radialGradient id="heroGlowB" cx="60%" cy="35%" r="70%">
          <stop offset="0" stop-color="#6aa2ff"/><stop offset=".5" stop-color="#1d5cc0"/><stop offset="1" stop-color="#0b2f86"/>
        </radialGradient>
      </defs>
      <path d="M0 0H560V250C450 300 300 330 0 350Z" fill="url(#heroGlowB)"/>
      <path d="M0 350C300 330 450 300 560 250V272C450 322 300 352 0 372Z" fill="#33a6d7"/>
      <path d="M0 372C300 352 450 322 560 272V286C450 336 300 366 0 386Z" fill="#33b8a4" opacity=".7"/>
    </svg>
    <div class="inset" role="img" aria-label="Close-up illustration of an inflamed elbow joint"></div>
    <div class="brand"><span class="dot"></span><span><span class="name">LONESTAR</span><small>Limb Clinic, L.L.P</small></span></div>
    <div class="title-block">
      <div class="doctor">DANIEL R. HASKELL, MD</div>
      <div class="specialty">SPECIALIST IN SURGERY</div>
      <div class="regions">OF THE HAND, WRIST, ELBOW &amp; SHOULDER</div>
      <div class="board">BOARD CERTIFIED ORTHOPEDIC SURGEON</div>
      <div class="cert">CERTIFICATE OF ADDITIONAL QUALIFICATION, HAND SURGERY</div>
    </div>
    <ul class="conditions">
      <li><svg class="tick" viewBox="0 0 10 10"><path d="M1 5l3 3 5-7" fill="none" stroke="#3a4150" stroke-width="1.6"/></svg>Carpal Tunnel</li>
      <li><svg class="tick" viewBox="0 0 10 10"><path d="M1 5l3 3 5-7" fill="none" stroke="#3a4150" stroke-width="1.6"/></svg>Cubital Tunnel</li>
      <li><svg class="tick" viewBox="0 0 10 10"><path d="M1 5l3 3 5-7" fill="none" stroke="#3a4150" stroke-width="1.6"/></svg>Trigger Finger</li>
      <li><svg class="tick" viewBox="0 0 10 10"><path d="M1 5l3 3 5-7" fill="none" stroke="#3a4150" stroke-width="1.6"/></svg>Dequervain's Tendinitis</li>
      <li><svg class="tick" viewBox="0 0 10 10"><path d="M1 5l3 3 5-7" fill="none" stroke="#3a4150" stroke-width="1.6"/></svg>Elbow &amp; Shoulder Pain</li>
    </ul>
    <div class="rule"></div>
    <div class="callbar">
      <span class="phone">555-014-ARMS</span>
      <span class="booking"><strong>Appointments can be made online</strong>through bookvisit.example www.MendLimbWellDallas.example</span>
    </div>
  </section>
</div>

<!-- Inside spread -->
<div class="spread spread-inside">
  <section class="page inside-left left">
    <svg class="abs" style="left:0;top:0" width="560" height="792" viewBox="0 0 560 792" aria-hidden="true">
      <rect x="-30" y="20" width="180" height="34" rx="17" fill="#33b8a4"/>
      <rect x="-40" y="66" width="150" height="34" rx="17" fill="#3176b5"/>
      <rect x="-30" y="112" width="120" height="34" rx="17" fill="#33a6d7"/>
      <rect x="-20" y="158" width="90" height="24" rx="12" fill="#33b8a4" opacity=".6"/>
      <path d="M0 610C180 590 380 600 560 620V792H0Z" fill="#33a6d7"/>
      <path d="M0 632C180 612 380 622 560 642V792H0Z" fill="#3176b5"/>
    </svg>
    <div class="carpal">
      <h2 class="section-title">CARPAL TUNNEL SYNDROME</h2>
      <div class="body-copy"><p>Carpal tunnel syndrome occurs when the median nerve is pinched as it passes through the wrist. It often leads to numbness and tingling in the thumb, index and middle fingers, and many patients notice it first at night or while gripping.</p></div>
    </div>
    <div class="carpal-more body-copy">
      <p>Unless the condition is caught early, symptoms can progress to weakness and loss of fine motor control. Splinting and activity changes may help, but when relief does not last, a short outpatient release can take pressure off the nerve and restore comfort.</p>
      <p>Our team offers both open and endoscopic techniques. To learn more, watch our patient videos at www.MendLimbWellDallas.example.</p>
    </div>
    <div class="arm-photo" role="img" aria-label="Photo of a patient holding a sore forearm and wrist"></div>
    <div class="pill">Cubital Tunnel Syndrome</div>
    <div class="cubital-copy body-copy">
      <p>Cubital tunnel syndrome occurs when the ulnar nerve is squeezed at the elbow, causing tingling in the ring and small fingers. Bending the elbow for long periods often makes it worse. Gentle splinting helps many people, and surgery is available when symptoms persist. Visit www.MendLimbWellDallas.example.</p>
    </div>
  </section>

  <section class="page inside-right right">
    <svg class="trigger-panel" viewBox="0 0 560 290" aria-hidden="true">
      <defs>
        <linearGradient id="tealPanel" x1="0" y1="0" x2="1" y2="1">
          <stop offset="0" stop-color="#33b8a4"/><stop offset="1" stop-color="#1f9a7a"/>
        </linearGradient>
      </defs>
      <path d="M0 0H560V290H0Z" fill="url(#tealPanel)"/>
      <path d="M0 0H280C200 20 120 30 0 36Z" fill="#ffffff"/>
    </svg>
    <div class="trigger">
      <h2 class="section-title">TRIGGER FINGER</h2>
      <div class="body-copy">
        <p>Trigger finger occurs when the tendon that bends the finger catches as it glides through its sheath. The finger may lock in a bent position and then snap straight, which can be painful and make gripping difficult throughout the day.</p>
        <p>Splinting and a single injection often ease the catching. If it returns, a brief release procedure usually solves the problem for good and allows a quick return to normal use.</p>
      </div>
    </div>
    <div class="thumbs">
      <div class="thumb-a" role="img" aria-label="Photo of a hand being examined"></div>
      <div class="thumb-b" role="img" aria-label="Photo of a person rubbing a sore shoulder"></div>
      <div class="thumb-c" role="img" aria-label="Photo of a person holding a painful elbow"></div>
    </div>
    <div class="wrist">
      <h2 class="section-title">WRIST PAIN</h2>
      <div class="body-copy">
        <p>Wrist pain may have many causes and the right diagnosis is best made by a fellowship trained hand surgeon. Dequervain's tendinitis causes pain on the thumb side of the wrist and is common in new parents and people who lift often.</p>
        <p>Most cases settle with rest, bracing and an injection. When they do not, a simple release can relieve the pain. To see a video of this procedure, please visit www.MendLimbWellDallas.example.</p>
      </div>
    </div>
    <div class="wrist-bar"></div>
  </section>
</div>

</body>
</html>
```